Design für Digitalisierungsprojekte
Zielgruppe
Wir sind der digitale Problemlöser, d.h. wir machen Digitalisierungsprojekte, von der Strategieberatung bis zur technischen Umsetzung und dem Kulturwandel. Wir machen individuelle Projekte, keine Produkte von der Stange. Unsere Kunden sind gehobener Mittelstand bis Konzern, ab 25 Mio € aufwärts. Oft sind unsere Kunden aus konservativen Branchen. Wir müssen beim Design immer einen Kompromiss aus innovativ und Vertrauen erweckend finden.
Aufgabenstellung
E-Book Design
Exo2 und open sans ist unsere Schriftart. Logos habe ich in 2 Formaten angehängt.
Auf den beiden Flyern angehängt finden Sie die Corporate Identity.
Ebook Inhalt ist im Anhang als Word Datei
Wenn Sie weitere Ideen haben, sind wir ganz Ohr.
Grafisch bitte nur die Farben grau, schwarz und orange verwenden (grau und orange siehe Logo)

```html
<!DOCTYPE html>
<html lang="de">
<head>
<meta charset="utf-8">
<title>NOVARA – Sicherheit in LoRaWAN Netzen – E-Book Seiten</title>
<link href="https://fonts.googleapis.com/css2?family=Exo+2:wght@500;600;700&family=Open+Sans:wght@400;600;700&display=swap" rel="stylesheet">
<style>
:root{
  --orange:#f47b20;
  --grey:#939598;
  --grey-light:#c8c8c8;
  --ink:#1e1e1e;
  --body:#3a3a3a;
  --paper:#ffffff;
  --photo-deep:#0d2a4f;
  --photo-mid:#3f7fb8;
}
*{margin:0;padding:0;box-sizing:border-box}
html,body{width:1200px;height:4012px;overflow:hidden}
body{background:var(--grey-light);position:relative;font-family:"Open Sans",sans-serif;color:var(--body)}
.page{position:absolute;background:var(--paper);overflow:hidden}
.spread-divider{position:absolute;width:2px;background:var(--grey-light)}
.tab{position:absolute;left:439px;top:0;width:45px;height:90px;background:var(--orange)}
.tab.grey{background:var(--grey)}
.footer{position:absolute;left:30px;right:33px;top:662px;display:flex;align-items:center;gap:6px}
.footer span{font-size:8px;color:var(--grey);letter-spacing:.3px}
.footer i{flex:1;height:2px;background:var(--grey)}
.footer b{width:10px;height:6px;background:var(--orange)}
.body-text{position:absolute;left:59px;width:425px;font-size:9.4px;line-height:17.6px;text-align:justify;color:var(--body)}
.body-text p{margin-bottom:17.6px}
.heading{font-family:"Exo 2",sans-serif;font-weight:600;color:var(--orange)}
.chapter{position:absolute;left:59px;top:72px;display:flex;gap:14px;align-items:flex-start}
.chapter .num{width:39px;height:39px;border-radius:50%;background:var(--grey);color:#fff;font-family:"Exo 2",sans-serif;font-weight:700;font-size:16px;display:flex;align-items:center;justify-content:center;margin-top:4px}
.chapter h2{font-family:"Exo 2",sans-serif;font-weight:600;color:var(--orange);font-size:20px;line-height:24px;width:310px}
ul.bullets{list-style:none}
ul.bullets li{position:relative;padding-left:14px;margin-bottom:17.6px}
ul.bullets li::before{content:"";position:absolute;left:0;top:6px;width:5px;height:5px;background:var(--orange)}
ol.alpha{list-style:none}
ol.alpha li{position:relative;padding-left:17px;margin-bottom:17.6px}
ol.alpha li span{position:absolute;left:0;color:var(--orange)}
.lead{font-weight:700;color:var(--ink)}
/* cover */
.cover-photo{position:absolute;left:33px;top:31px;width:481px;height:492px;background:radial-gradient(circle at 70% 30%,#8fc3e8 0%,var(--photo-mid) 30%,var(--photo-deep) 80%)}
.cover-logo-box{position:absolute;left:33px;top:31px;width:138px;height:120px;background:var(--paper)}
.brand{font-family:"Exo 2",sans-serif;font-weight:600;color:var(--orange);letter-spacing:4px;display:flex;align-items:center;gap:6px}
.brand-sub{font-family:"Exo 2",sans-serif;font-weight:600;color:var(--orange);font-size:6px;letter-spacing:.4px;margin-top:4px}
.brand-dot{width:8px;height:8px;border-radius:50%;background:var(--orange)}
.title-box{position:absolute;background:var(--paper)}
.title-box .t-dark{font-family:"Exo 2",sans-serif;font-weight:600;color:var(--ink)}
.title-box .t-orange{font-family:"Exo 2",sans-serif;font-weight:600;color:var(--orange)}
.rule{height:5px;background:var(--orange)}
/* toc */
.toc{position:absolute;left:31px;top:90px;width:481px;height:540px;border:9px solid var(--orange)}
.toc h2{position:absolute;left:45px;top:60px;font-family:"Exo 2",sans-serif;font-weight:700;color:var(--orange);font-size:26px;width:375px;border-bottom:2px solid var(--orange);padding-bottom:2px}
.toc ol{position:absolute;left:45px;top:116px;width:395px;list-style:none}
.toc li{font-size:9.4px;color:var(--body);height:43px;padding-top:8px;border-bottom:1px solid #ececec}
/* back */
.back-frame{position:absolute;left:33px;top:31px;width:481px;height:495px;background:var(--grey)}
.back-inner{position:absolute;left:92px;top:89px;width:362px;height:383px;background:var(--paper)}
.back-photo{position:absolute;left:233px;top:160px;width:207px;height:252px;background:linear-gradient(135deg,#3a2a22 0%,#7a5a40 40%,#d8b080 75%,#f2dcc0 100%)}
.back-logo{position:absolute;left:112px;top:120px;width:121px;height:111px;background:var(--orange);padding:30px 12px 0}
.contact{position:absolute;left:187px;top:540px;width:210px;font-size:7.5px;line-height:14px;color:var(--ink)}
.contact .bar{background:var(--orange);color:#fff;font-weight:700;padding-left:3px;height:11px;line-height:11px;margin-bottom:3px}
.contact div{display:flex;align-items:center;gap:5px}
</style>
</head>
<body>

<!-- Cover -->
<section class="page" style="left:327px;top:117px;width:546px;height:705px">
  <div class="cover-photo" role="img" aria-label="Foto: Hand berührt ein digitales Netzwerk aus Lichtpunkten über einer Weltkarte in Blautönen"></div>
  <div class="cover-logo-box">
    <div style="position:absolute;left:8px;top:42px">
      <div class="brand" style="font-size:24px">NOVARA<span class="brand-dot"></span></div>
      <div class="brand-sub">DIGITAL PROJECT PARTNERS</div>
    </div>
  </div>
  <div class="title-box" style="left:218px;top:345px;width:246px;height:178px;padding:27px 0 0 16px">
    <div class="t-dark" style="font-size:25px;line-height:28px">Sicherheit in</div>
    <div class="t-orange" style="font-size:38px;line-height:37px">LoRaWAN<br>Netzen</div>
    <div class="t-dark" style="font-size:31px;line-height:36px">ein Überblickt</div>
    <div class="rule" style="width:76px;height:4px;margin-top:10px"></div>
  </div>
  <div style="position:absolute;left:235px;top:601px;font-size:8.5px;line-height:12px;color:var(--ink)">
    Autor: Marlene Kessing, Geschäftsführerin<br>NOVARA GmbH 6.5.2019
  </div>
  <div class="rule" style="position:absolute;left:218px;top:638px;width:246px;height:8px"></div>
</section>

<!-- Spread 1 -->
<section class="page" style="left:51px;top:893px;width:546px;height:704px">
  <div class="tab"></div>
  <h1 class="heading" style="position:absolute;left:59px;top:72px;font-size:19px">Think Global Act Local</h1>
  <div class="body-text" style="top:102px">
    <p>LoRaWAN steht für Long Range Wide Area Network und ist eine Technologie zur Datenübertragung für Internet of Things Anwendungen. Für einige Anwendungen wird es als Alternative zu Mobilfunk genutzt. Doch ist es eine echte Alternative? Kann LoRaWAN sicher genutzt werden, oder kann jeder Hacker die Daten mitlesen?</p>
    <p>Zur Beurteilung der Bedrohung durch Angreifer beschäftigt sich dieser Artikel zunächst mit der Motivation und dem Schaden, den Angreifer anrichten würden. Aufgrund der heute überwiegend regionalen Einsatzgebiete von LoRaWAN, und aufgrund der Limitierungen auf kleine Datenmengen, ist LoRaWAN für Angreifer derzeit nicht der attraktivste Angriffspunkt. Die Infrastruktur dahinter jedoch, die für Anwendungen mit verschiedenen Übertragungstechnologien genutzt wird, kann ein attraktives Angriffsziel sein.</p>
    <p>Der Schaden, der durch Angriffe bewirkt werden kann, muss für jeden Fall einzeln bewertet werden. Eine allgemeine Aussage für die Schadenshöhe kann nicht getroffen werden. Allgemein gilt nur, dass der Schaden bei einem Angriff auf die Internet of Things-Server, in der Regel höher ist als der Schaden bei einem Angriff auf die LoRaWAN-Endgeräte.</p>
    <p>In diesem Artikel wird die LoRaWAN-Architektur beleuchtet, sowie die eingebauten Sicherheitsmechanismen. LoRaWAN bringt bereits sehr gute Sicherheitsmechanismen mit, wie z.B. AES-128 Nachrichtenverschlüsselung. Diese kann bis heute nicht ausgehebelt werden, sofern sie korrekt und mit entsprechenden Vorsichtsmaßnahmen implementiert wird. Die Schwachstellen liegen eher im Bereich der Hardware, weil hier nur weniger konkrete Standards für sichere Implementierung vorliegen. In Kombination mit unvorsichtigen Implementierungen, z.B. schlecht gesicherten Gateway oder Geräte-Standorten, können diese Schwachstellen ausgenutzt werden.</p>
  </div>
  <div class="footer"><span>NOVARA</span><i></i></div>
</section>
<div class="spread-divider" style="left:597px;top:893px;height:704px"></div>
<section class="page" style="left:599px;top:893px;width:543px;height:704px">
  <div class="tab grey"></div>
  <div class="body-text" style="top:102px">
    <p>Für eine sichere LoRaWAN-Implementierung ist es nicht notwendig, ein weiteres Verschlüsselungsprotokoll, wie z.B. TLS-Verschlüsselung, zu verwenden, da AES-128 selbst sicher ist und in sicherheitsrelevanten Anwendungen weit verbreitet ist. Es ist jedoch notwendig sehr gutes Schlüsselmanagement, professionelle Sicherheitsprozesse und gute physische Sicherheit zu implementieren, sowie das Netz redundant und relativ engmaschig aufzubauen. Bei der Auswahl der Hardware, der Server, der Rechenzentren und der Software muss auf entsprechende Sicherheitsvorkehrungen geachtet werden. Die Kommunikation zwischen dem LoRaWAN und dem Rest der Infrastruktur muss entsprechend abgesichert werden.</p>
    <p>Es ist möglich, mit bestehender, nicht-proprietärer Technologie eine sichere, zuverlässige Internet of Things-Anwendung mit Kommunikation über LoRaWAN aufzubauen.</p>
  </div>
  <div class="footer"><span>NOVARA</span><i></i></div>
</section>

<!-- Spread 2 -->
<section class="page" style="left:51px;top:1670px;width:546px;height:704px">
  <div class="toc">
    <h2>Inhalte</h2>
    <ol>
      <li>1. LoRaWAN – Eigenschaften und Anwendungsfälle</li>
      <li>2. Motivation für Angriffe auf LoRaWAN Netze – Nutzen des Angreifers</li>
      <li>3. Schaden durch Angriffe auf LoRaWAN-Netzwerke für den Nutzer oder Betreiber</li>
      <li>4. LoRaWAN 1.0 Architektur und Stack</li>
      <li>5. In LoRaWAN 1.0 eingebaute Sicherheitsmechanismen</li>
      <li>6. Schwachstellen und Angriffsarten</li>
      <li>7. Empfehlungen</li>
      <li style="border-bottom:none">8. Schlussfolgerungen</li>
    </ol>
  </div>
  <div class="footer"><span>NOVARA</span><i></i></div>
</section>
<div class="spread-divider" style="left:597px;top:1670px;height:704px"></div>
<section class="page" style="left:599px;top:1670px;width:543px;height:704px">
  <div class="tab"></div>
  <div class="chapter"><div class="num">1.</div><h2>LoRaWAN – Eigenschaften und Anwendungsfälle</h2></div>
  <div class="body-text" style="top:144px;font-size:9.2px">
    <p class="lead">LoRaWAN ist eine Funktechnologie zur Übertragung von Maschinen-, Geräte- und Gebäudedaten. Seine Haupteigenschaften sind:</p>
    <ul class="bullets">
      <li>Hohe Reichweite – theoretisch bis zu 30km, praktisch im städtischen Bereich ca. 1-3km, im ländlichen Bereich mit freier Sicht bis zu 15km</li>
      <li>Sehr niedriger Stromverbrauch, d.h. die Lebensdauer der Endgeräte ist vor allem durch die Frequenz und Dauer der Datenübertragung bestimmt. Bei üblichen Anwendungen können Laufzeiten von bis zu 10 Jahren erreicht werden.</li>
      <li>Geringe Datenraten, d.h. es können nur geringe Datenmengen übertragen werden. Eine kontinuierliche Übertragung, wie einer Live-Videoüberwachung ist nicht möglich.</li>
      <li>Freies Spektrum – LoRaWAN Netze dürfen frei aufgebaut und genutzt werden. Für das Funkspektrum fallen keine Nutzungsgebühren an, aber es gibt auch niemanden, der eine Garantie für die Übertragung übernimmt.</li>
      <li>Bidirektionale Datenübertragung, das heißt sowohl Auslesung von Daten als auch Steuerung von Aktionen sind möglich, mit den Limitierungen von Funknetzen allgemein.</li>
    </ul>
    <p class="lead">Durch diese Eigenschaften ergeben sich unter anderem folgende Anwendungsfälle (Beispiele):</p>
    <ul class="bullets">
      <li>Überwachung von Netzen und Infrastruktur, z.B. Strom-, Gas-, Wasser-, Fernwärme-, Kanalnetze, Brücken, Straßen uvm.</li>
    </ul>
  </div>
  <div class="footer"><span>NOVARA</span><i></i><b></b></div>
</section>

<!-- Spread 3 -->
<section class="page" style="left:51px;top:2444px;width:546px;height:703px">
  <div class="tab grey"></div>
  <div class="body-text" style="top:100px;font-size:9.2px">
    <ul class="bullets">
      <li>Vollautomatische Zählerablesung</li>
      <li>Gebäudeüberwachung: Eindringlinge feststellen, Funktion von Licht, Aufzug, Klimaanlage etc., Raumklima, Raumbelegung überwachen</li>
      <li>Vorausschauende Wartung, z.B. von Klimaanlagen, bei denen das Zusetzen des Filters gemessen und daraus die Wartungsnotwendigkeit und gute Wartungsintervalle für individuelle Geräte gelernt werden</li>
      <li>Smart City Anwendungen wie Smart Parking, Routenoptimierung von Entsorgungsfahrzeugen, Beleuchtung, uvm.</li>
      <li>Smart Farming durch Überwachung von Bodeneigenschaften, Tracking und Gesundheitszustand der Tiere etc.</li>
      <li>Fahrzeug- oder Personenzählung, z.B. für Besucher, Durchgangsverkehr etc.</li>
    </ul>
    <p>Die erste Version von LoRaWAN – LoRaWAN 1.0 – wurde 2013 patentiert und wird seit 2015 kommerziell genutzt. Bereits 2017 wurde LoRaWAN 1.1 spezifiziert, ist aber bisher noch nicht weitreichend implementiert. Bisherige Server und Endgeräte laufen fast ausschließlich auf LoRaWAN 1.0. Deshalb bezieht sich dieses Paper auf LoRaWAN 1.0.</p>
    <p>Um eine vollständige Internet of Things-Anwendung aufzubauen und zu betreiben, werden neben LoRaWAN-Sensoren und -Gateways weitere Komponenten benötigt. Dieses Paper beschäftigt sich im Schwerpunkt mit der Sicherheit der Kommunikation über LoRaWAN, am Rande mit der gesamten Architektur von Internet of Things-Anwendungen.</p>
  </div>
  <div class="footer"><span>NOVARA</span><i></i><b></b></div>
</section>
<div class="spread-divider" style="left:597px;top:2444px;height:703px"></div>
<section class="page" style="left:599px;top:2444px;width:543px;height:703px">
  <div class="tab"></div>
  <div class="chapter"><div class="num">2.</div><h2>Motivation für Angriffe auf LoRaWAN Netze – Nutzen des Angreifers</h2></div>
  <div class="body-text" style="top:164px;font-size:9.2px">
    <p>Die erste Überlegung bei Sicherheitsbetrachtungen muss immer die Motivation von Angreifern sein: Welche Personengruppen oder Organisationen haben ein Interesse daran, ein System zu hacken, und welchen Vorteil erhoffen sie sich.</p>
    <p>Ebenfalls entscheidend ist, welchen Schaden sie mit einem Angriff anrichten können.</p>
    <p>Aus diesen beiden Überlegungen lässt sich ableiten, wieviel Aufwand in die Sicherheitsmechanismen eines Systems gesteckt werden muss.</p>
    <p>Aufgrund seiner Eigenschaften ist LoRaWAN eine beliebte Technologie im Versorger- und Smart City-Umfeld. Die Motivationsbetrachtung bezieht sich daher in diesem White Paper vor allem auf Versorger.</p>
    <p>Versorger können LoRaWAN grundsätzlich in drei Anwendungsbereichen nutzen.</p>
    <ol class="alpha">
      <li><span>a.</span>Eigenbedarf – Steigerung der Effizienz der eigenen Abläufe. Hierzu zählen Themen wie Netz- und Infrastrukturüberwachung, Eindringlings-Detektion, Fernablesung von Zählerständen, Leckagen-Detektion, Gebäudemanagement uvm.</li>
      <li><span>b.</span>Vermietung des Netzes an öffentliche oder private Unternehmen</li>
      <li><span>c.</span>Anbieten von kompletten Lösungen, z.B. für Smart City oder die Wohnungswirtschaft</li>
    </ol>
  </div>
  <div class="footer"><span>NOVARA</span><i></i><b></b></div>
</section>

<!-- Back cover -->
<section class="page" style="left:327px;top:3206px;width:546px;height:704px">
  <div class="back-frame"></div>
  <div class="back-inner"></div>
  <div class="back-photo" role="img" aria-label="Foto: Hände an einem Laptop mit eingeblendeten digitalen Symbolen in warmen Brauntönen"></div>
  <div class="back-logo">
    <div class="brand" style="font-size:16px;color:#fff;letter-spacing:2.5px;gap:4px">NOVARA<span class="brand-dot" style="background:#fff;width:6px;height:6px"></span></div>
    <div class="brand-sub" style="color:#fff;font-size:4.5px">DIGITAL PROJECT PARTNERS</div>
  </div>
  <div class="title-box" style="left:128px;top:231px;width:199px;height:127px;padding:14px 0 0 14px">
    <div class="t-dark" style="font-size:16px;line-height:18px">Sicherheit in</div>
    <div class="t-orange" style="font-size:25px;line-height:24px">LoRaWAN<br>Netzen</div>
    <div class="t-dark" style="font-size:20px;line-height:25px">ein Überblickt</div>
  </div>
  <div class="contact">
    <div class="bar">Contact Us</div>
    <div style="font-weight:700">NOVARA GmbH Lindenweg 12 40213 Düsseldorf</div>
    <div><svg width="8" height="8" viewBox="0 0 10 10"><path d="M2 1l2 0 1 2.5-1.3 1a6 6 0 0 0 2.8 2.8l1-1.3L10 7v2a1 1 0 0 1-1 1A9 9 0 0 1 1 2a1 1 0 0 1 1-1z" fill="none" stroke="#1e1e1e" stroke-width="1"/></svg>+49 211 5550190</div>
    <div><svg width="8" height="8" viewBox="0 0 10 10"><rect x="0.5" y="2" width="9" height="6.5" fill="none" stroke="#1e1e1e"/><path d="M0.5 2l4.5 3.5L9.5 2" fill="none" stroke="#1e1e1e"/></svg>kontakt@novara-digital.example</div>
  </div>
  <div style="position:absolute;left:151px;top:619px;width:246px;height:8px;background:var(--grey)"></div>
</section>

</body>
</html>
```